K&T Fire Safety Equipment Inc. needs an updated/new website design

I would like the customer to be able to see who we are, where are are, what we do and areas we cover on the first page. I would like something modern but professional. The other fire safety companies out there have very boring & unappealing websites. I want mine seem like we've got it together and to be above average in comparison. I would like the colors to go with our logo and would like to incorporate somewhere that we have been in business for over 30 years, we are family owned and operated and that we provide service to all of central Florida from Tampa to Titusville and all of Brevard county (we can take out the" all of Brevard county" but keep the " All of Central Florida from Tampa to Titusville" and just add all counties we service to the very bottom too). We are a residential and commercial fire safety equipment company. We do sales, service and installation for fire extinguishers, emergency/exit lighting, kitchen fire suppression systems, fire alarms & fire extinguisher cabinets.I have also attached some pictures that you can use to incorporate any way you would like. Here's our current website (awful I know) to get information from if needed. kandtfiresafety.example

Target Market(s)

Restaurants, hotels, vacation rental properties & small businesses. Every business is required to have a fire extinguisher and exit lighting.

Industry/Entity Type

Fire Safety

Number of Pages Required

1 page

Font styles to use
Other font styles liked:
• I'm open to your suggestions

Colors

Designer to choose colors to be used in the design.

Requirements
Must have
• I would like the customer to be able to see who we are, where are are, what we do and areas we cover on the first page. I would like the colors to go with our logo and would like to incorporate somewhere that we have been in business for over 30 years, we are family owned and operated and that we provide service to all of central Florida from Tampa to Titusville and all of Brevard county (we can take out the" all of Brevard county" but keep the " All of Central Florida from Tampa to Titusville" and just add all counties we service to the very bottom too)
Nice to have
• Modern with high quality pictures
• I love the raised logo that I added in the attachments. If you could make the logo look like that in incorporate it as one of the first things you see that would be awesome!
• I would eventually like to have a portfolio of work completed on an additional page.
Should not have
• boring outdated look

```html
<!DOCTYPE html>
<html lang="en">
<head>
<meta charset="utf-8">
<title>K&amp;T Fire Safety Equipment Inc.</title>
<link href="https://fonts.googleapis.com/css2?family=Lato:wght@400;700&family=Roboto:wght@400;500;700&display=swap" rel="stylesheet">
<style>
:root{
  --orange:#f07a1e;
  --red:#d92828;
  --ink:#222;
  --text:#444;
  --muted:#777;
  --dark:#1f1f1f;
  --darker:#161616;
  --line:#d7d7d7;
  --white:#fff;
}
*{box-sizing:border-box;margin:0;padding:0}
html,body{width:1200px;height:3315px;overflow:hidden}
body{position:relative;background:var(--white);font-family:"Lato",Arial,sans-serif;color:var(--text)}
.abs{position:absolute}
h2{font-family:"Roboto",Arial,sans-serif;font-weight:400}

/* hero */
.hero{left:0;top:0;width:1200px;height:585px;background:linear-gradient(120deg,#f3ece6 0%,#f6d9b8 45%,#f2b46a 75%,#e98a3a 100%)}
.brand{left:88px;top:40px;width:200px;font-family:"Lato",Arial,sans-serif;font-weight:700;font-size:17px;line-height:1.25;color:var(--ink);display:flex;align-items:center;gap:10px}
.brand .dot{width:26px;height:26px;background:var(--red);flex:none}
.emergency{left:592px;top:12px;font-size:13px;color:var(--ink);display:flex;align-items:center;gap:10px}
.emergency b{font-weight:700}
.nav{left:550px;top:68px;display:flex;gap:40px;font-size:13.5px;text-transform:uppercase;color:var(--ink)}
.nav a{color:inherit;text-decoration:none;padding-bottom:5px}
.nav a.active{border-bottom:2px solid var(--ink)}
.hero-photo{left:77px;top:155px;width:470px;height:420px;background:radial-gradient(ellipse at 50% 55%,#d62a2a 0%,#b51f1f 40%,rgba(180,40,40,0) 72%)}
.hero-copy{left:548px;top:262px;width:560px}
.hero-copy .kicker{font-family:"Roboto",Arial,sans-serif;font-weight:700;font-size:30px;color:#333;line-height:1.1}
.hero-copy .title{font-family:"Roboto",Arial,sans-serif;font-weight:700;font-size:33px;color:var(--red);line-height:1.2;margin-bottom:10px}
.hero-copy p{font-size:13.5px;line-height:1.6;color:#333}
.dots{left:1053px;top:555px;display:flex;gap:5px}
.dots span{width:15px;height:15px;background:#aaa}
.dots span:first-child{background:var(--red)}

/* about */
.about-bg{left:0;top:720px;width:260px;height:230px;background:linear-gradient(90deg,rgba(220,80,80,.12),rgba(220,80,80,0))}
.about-title{left:88px;top:628px;font-size:32px;color:var(--orange)}
.about-text{left:88px;top:690px;width:690px;font-size:12.6px;line-height:1.75;color:#333}
.about-photo{left:840px;top:652px;width:272px;height:243px;background:linear-gradient(135deg,#e8ecee 0%,#d9dde0 40%,#c63030 70%,#a51d1d 100%);box-shadow:0 3px 8px rgba(0,0,0,.25)}

/* services */
.services{left:0;top:946px;width:1200px;height:879px;background:linear-gradient(180deg,#2a2a2a,#1b1b1b)}
.services h2{position:absolute;left:0;width:1200px;top:42px;text-align:center;font-size:33px;color:var(--white)}
.card{width:323px;height:235px;border:1px solid #cfcfcf;text-align:center;color:var(--white)}
.card .pic{position:absolute;left:71px;top:-69px;width:180px;height:130px;border:2px solid #fff}
.card h3{position:absolute;top:80px;width:100%;font-family:"Lato",Arial,sans-serif;font-weight:400;font-size:15px;text-transform:uppercase}
.card p{position:absolute;top:112px;left:22px;right:22px;font-size:12.6px;line-height:1.7}
.btn{display:flex;align-items:center;justify-content:center;background:var(--red);color:var(--white);font-weight:700;font-size:13px;text-transform:uppercase}

/* testimonials */
.t-title{left:0;width:1200px;top:1870px;text-align:center;font-size:31px;color:var(--orange)}
.quote{left:0;width:1200px;top:1925px;text-align:center;font-family:Georgia,serif;font-size:44px;color:var(--orange);line-height:1}
.t-text{left:287px;top:1968px;width:630px;text-align:center;font-size:12.6px;line-height:1.85;color:#555}
.t-rule{left:558px;top:2058px;width:84px;height:1px;background:var(--line)}
.t-name{left:0;width:1200px;top:2067px;text-align:center;font-size:12.5px;color:#555;text-transform:uppercase}
.avatar{border-radius:50%;background:radial-gradient(circle,#b9c2c9,#7e8a94)}

/* contact */
.contact{left:0;top:2223px;width:1200px;height:380px;background:linear-gradient(180deg,#3a3030,#241f1f)}
.contact h2{position:absolute;left:0;width:1200px;top:40px;text-align:center;font-size:33px;color:var(--white)}
.field{background:rgba(255,255,255,.3);color:#eee;font-size:13px;padding:12px 12px}

/* map & footer */
.map{left:0;top:2603px;width:1200px;height:363px;background:linear-gradient(135deg,#eef0ec 0%,#e4e8e2 50%,#dfe6ea 100%)}
.footer{left:0;top:2966px;width:1200px;height:349px;background:linear-gradient(180deg,#1d1a19,#2a1e18)}
.footer-brand{left:88px;top:3040px;width:180px;font-weight:700;font-size:17px;line-height:1.25;color:var(--white)}
.f-head{font-family:"Roboto",Arial,sans-serif;font-weight:500;font-size:15px;color:var(--orange);line-height:1.3}
.f-item{font-size:13px;color:var(--white);display:flex;align-items:center;gap:14px}
.hours{left:678px;top:3046px;font-size:13px;color:var(--white)}
.hours div{display:flex;width:180px;justify-content:space-between;height:47px}
.f-rule{left:0;top:3266px;width:1200px;height:1px;background:rgba(255,255,255,.15)}
.copy{left:0;width:1200px;top:3281px;text-align:center;font-size:13px;color:var(--white)}
</style>
</head>
<body>

<!-- hero -->
<div class="abs hero" role="img" aria-label="Background photo of orange flames"></div>
<div class="abs brand"><span class="dot"></span><span>K&amp;T Fire Safety Equipment Inc.</span></div>
<div class="abs emergency">
  <svg width="22" height="22" viewBox="0 0 24 24" fill="none" stroke="#222" stroke-width="1.8"><path d="M5 3h4l2 5-2.5 1.5a11 11 0 0 0 6 6L16 13l5 2v4a2 2 0 0 1-2 2A16 16 0 0 1 3 5a2 2 0 0 1 2-2z"/></svg>
  <b>24 HOUR EMERGENCY PHONE NUMBER</b><span>:</span><span>1-407-555-0148 , 1-407-555-0162</span>
</div>
<nav class="abs nav">
  <a class="active">Home</a><a>About</a><a>Our Trucks &amp; Teams</a><a>Book Online</a><a>Moving Tips</a>
</nav>
<div class="abs hero-photo" role="img" aria-label="Photo of red fire extinguishers"></div>
<div class="abs hero-copy">
  <div class="kicker">DEDICATED TO</div>
  <div class="title">PROTECTING LIFE AND PROPERTY</div>
  <p>Lorem Ipsum is simply dummy text of the printing and typesetting industry. Lorem Ipsum has been the industry's standard dummy text ever since the 1500s, when an unknown printer took a galley of type and scrambled it to make a type specimen book. It has survived not only five centuries.</p>
</div>
<div class="abs dots"><span></span><span></span><span></span></div>

<!-- about -->
<div class="abs about-bg" role="img" aria-label="Faint photo of a fire extinguisher"></div>
<h2 class="abs about-title">ABOUT US</h2>
<p class="abs about-text">We have been providing fire protection to Central Florida for over 30 years! &nbsp; K&amp;T Fire Safety is family owned and operated. We provide quality service, professional fire protection and life safety to meet the needs of our community. We provide residential and commercial fire protection to all of Brevard County and Central Florida from Tampa to Titusville. Our staff is exceptionally knowledgeable in fire safety and protection. Please feel free to contact us with any questions or concerns.</p>
<div class="abs about-photo" role="img" aria-label="Photo of a technician servicing a fire extinguisher"></div>

<!-- services -->
<section class="abs services" role="group" aria-label="Our services">
  <div class="abs" style="inset:0;background:linear-gradient(180deg,rgba(60,60,60,.4),rgba(0,0,0,0))" role="img" aria-label="Dark background photo of a warehouse interior"></div>
  <h2>OUR SERVICES</h2>
</section>

<div class="abs card" style="left:88px;top:1125px"><div class="pic" style="background:linear-gradient(135deg,#2b1a1a,#8a1f1f 50%,#1e5c2a)" role="img" aria-label="Photo of exit signs"></div><h3>Exit Lighting</h3><p>Lorem Ipsum is simply dummy text of the printing and typesetting industry. Lorem Ipsum has been the industry's standard dummy text ever since the 1500s.</p></div>
<div class="abs card" style="left:437px;top:1125px"><div class="pic" style="background:linear-gradient(135deg,#e05a5a,#b81d1d)" role="img" aria-label="Photo of red fire lettering"></div><h3>Exit Lighting</h3><p>Lorem Ipsum is simply dummy text of the printing and typesetting industry. Lorem Ipsum has been the industry's standard dummy text ever since the 1500s.</p></div>
<div class="abs card" style="left:789px;top:1125px"><div class="pic" style="background:linear-gradient(135deg,#c22a2a,#d9d9d9 70%)" role="img" aria-label="Photo of a fire alarm box"></div><h3>Exit Lighting</h3><p>Lorem Ipsum is simply dummy text of the printing and typesetting industry. Lorem Ipsum has been the industry's standard dummy text ever since the 1500s.</p></div>
<div class="abs card" style="left:88px;top:1463px"><div class="pic" style="background:linear-gradient(135deg,#9aa0a4,#d04a3a 60%,#c9c2bd)" role="img" aria-label="Photo of a kitchen suppression system"></div><h3>Exit Lighting</h3><p>Lorem Ipsum is simply dummy text of the printing and typesetting industry. Lorem Ipsum has been the industry's standard dummy text ever since the 1500s.</p></div>
<div class="abs card" style="left:437px;top:1463px"><div class="pic" style="background:linear-gradient(135deg,#6b4a30,#b8906a 55%,#d9c6a8)" role="img" aria-label="Photo of a commercial kitchen"></div><h3>Exit Lighting</h3><p>Lorem Ipsum is simply dummy text of the printing and typesetting industry. Lorem Ipsum has been the industry's standard dummy text ever since the 1500s.</p></div>
<div class="abs card" style="left:789px;top:1463px"><div class="pic" style="background:linear-gradient(135deg,#2d3440,#707a86 55%,#c9ccd0)" role="img" aria-label="Photo of a technician at a fire alarm panel"></div><h3>Exit Lighting</h3><p>Lorem Ipsum is simply dummy text of the printing and typesetting industry. Lorem Ipsum has been the industry's standard dummy text ever since the 1500s.</p></div>

<div class="abs btn" style="left:544px;top:1735px;width:112px;height:37px">View More</div>

<!-- testimonials -->
<h2 class="abs t-title">TESTIMONIALS</h2>
<div class="abs quote">&ldquo;</div>
<p class="abs t-text">Printing and typesetting industry. Lorem Ipsum has been the industry's standard dummy text ever since the 1500s, when an unknown printer took a galley of type and scrambled. Lorem Ipsum is simply dummy text of the printing unknown printer took a galley of type and scrambled it to make a type .</p>
<div class="abs t-rule"></div>
<div class="abs t-name">Sam Carter</div>
<svg class="abs" style="left:424px;top:2128px" width="16" height="24" viewBox="0 0 16 24"><path d="M12 3 4 12l8 9" fill="none" stroke="#f07a1e" stroke-width="2"/></svg>
<svg class="abs" style="left:760px;top:2128px" width="16" height="24" viewBox="0 0 16 24"><path d="m4 3 8 9-8 9" fill="none" stroke="#f07a1e" stroke-width="2"/></svg>
<div class="abs avatar" style="left:496px;top:2115px;width:50px;height:50px" role="img" aria-label="Customer portrait"></div>
<div class="abs avatar" style="left:571px;top:2110px;width:60px;height:60px;border:3px solid #3aa0d8" role="img" aria-label="Customer portrait, selected"></div>
<div class="abs avatar" style="left:654px;top:2115px;width:50px;height:50px" role="img" aria-label="Customer portrait"></div>

<!-- contact -->
<section class="abs contact" role="group" aria-label="Contact us">
  <div class="abs" style="inset:0;background:linear-gradient(90deg,rgba(120,40,30,.25),rgba(0,0,0,0) 50%,rgba(120,40,30,.2))" role="img" aria-label="Dark background photo of a fire truck"></div>
  <h2>CONTACT US</h2>
</section>
<div class="abs field" style="left:88px;top:2331px;width:323px;height:40px">Name</div>
<div class="abs field" style="left:437px;top:2331px;width:323px;height:40px">Email</div>
<div class="abs field" style="left:789px;top:2331px;width:323px;height:40px">Phone</div>
<div class="abs field" style="left:88px;top:2398px;width:1024px;height:88px">Message</div>
<div class="abs btn" style="left:544px;top:2513px;width:112px;height:37px">Submit</div>

<!-- map -->
<div class="abs map" role="img" aria-label="Street map showing the office location in Kissimmee"></div>

<!-- footer -->
<footer class="abs footer" role="group" aria-label="Footer">
  <div class="abs" style="inset:0;background:linear-gradient(0deg,rgba(200,80,30,.18),rgba(0,0,0,0) 60%)" role="img" aria-label="Dark background with faint flames"></div>
</footer>
<div class="abs footer-brand">K&amp;T Fire Safety Equipment Inc.</div>

<div class="abs f-head" style="left:318px;top:2997px">Our Address</div>
<div class="abs f-item" style="left:318px;top:3043px">
  <svg width="14" height="14" viewBox="0 0 24 24" fill="#f07a1e"><path d="M5 2h4l2 6-3 2a12 12 0 0 0 6 6l2-3 6 2v4a3 3 0 0 1-3 3A18 18 0 0 1 2 5a3 3 0 0 1 3-3z"/></svg>1-407-555-0193</div>
<div class="abs f-item" style="left:318px;top:3082px">
  <svg width="14" height="12" viewBox="0 0 24 20" fill="#f07a1e"><path d="M0 2h24v16H0z"/><path d="M0 2l12 9 12-9" fill="none" stroke="#2a1e18" stroke-width="2"/></svg>ktfiresafety@example.com</div>
<div class="abs f-item" style="left:318px;top:3121px">
  <svg width="12" height="16" viewBox="0 0 16 22" fill="#f07a1e"><path d="M8 0a8 8 0 0 0-8 8c0 6 8 14 8 14s8-8 8-14a8 8 0 0 0-8-8zm0 11a3 3 0 1 1 0-6 3 3 0 0 1 0 6z"/></svg>482 N Orange Ave, Kissimmee, FL 34741, USA</div>

<div class="abs f-head" style="left:678px;top:2997px">Hours of Operation</div>
<div class="abs hours">
  <div><span>Monday</span><span>8 a.m - 4 p.m</span></div>
  <div><span>Tuesday</span><span>8 a.m - 4 p.m</span></div>
  <div><span>Wednesday</span><span>8 a.m - 4 p.m</span></div>
  <div><span>Thursday</span><span>8 a.m - 4 p.m</span></div>
  <div><span>Friday</span><span>8 a.m - 4 p.m</span></div>
</div>

<div class="abs f-head" style="left:926px;top:2997px">24 Hour Emergency<br>Phone Number</div>
<div class="abs f-item" style="left:926px;top:3046px">1-407-555-0162</div>

<div class="abs f-rule"></div>
<div class="abs copy">&copy; 2018. My company. All Rights Reserved.</div>

</body>
</html>
```